Book cover for The Quiet Harbor Method to Grow a Fearless Venture

Book cover design for soft cover non-fiction book.

The front cover is what is most important at this stage, I am still gathering the testimonials and book description for the back cover so a rough to be completed later for the back is great.

Title as per above. Divided up "The Quiet Harbor Method" (to be a series) and "Grow a Fearless Venture" in this book in the series

Also for the front:

Corla Vennick

"The most unusual business book you will read." - Jodi Marquenthal, Author of Founder Tidewalk

Background info:

This work is a blending of the masculine and feminine energies, the practical business skills with a strong focus on the inner game. I am looking for the cover to have a nod to the Dominatrix and a clear message that one can be soft (kind, open hearted) and still be strong and firm in business.

Photo options are in this file https://www.filecrate-share.example/sh/qk41mxw07trbvle/BBFupdmWqYrLs3NxKeei47K5b?dl=0

Size 6" x 9" 179 pgs

Target Market(s)

female entreprenures

Industry/Entity Type

Business

Colors

Designer to choose colors to be used in the design.

Requirements
Must have
• I would like the title to be in a font that is bold and upscale, to contrast the softness fo the image.
• Clear and readable
• Unique look that will stand out
Should not have
• overt Dominatrix images or slant. It is about the energy not the actual.

```html
<!DOCTYPE html>
<html lang="en">
<head>
<meta charset="utf-8">
<title>The Quiet Harbor Method – Book Cover</title>
<link rel="stylesheet" href="https://fonts.googleapis.com/css2?family=Cinzel:wght@700;900&family=Roboto:wght@300&display=swap">
<style>
  :root {
    --backdrop: #b0b436;
    --cover-top: #0a0b0f;
    --cover-mid: #1c2740;
    --cover-bottom: #465b88;
    --ink-light: #ffffff;
    --ink-soft: #eef1f7;
    --photo-dark: #2a2230;
    --photo-red: #c8231f;
    --photo-plaid: #7a1f24;
  }
  html, body {
    margin: 0;
    padding: 0;
    width: 1200px;
    height: 1200px;
    overflow: hidden;
    background: var(--backdrop);
  }
  .canvas {
    position: relative;
    width: 1200px;
    height: 1200px;
    background: var(--backdrop);
  }
  .cover {
    position: absolute;
    left: 252px;
    top: 89px;
    width: 692px;
    height: 1017px;
    overflow: hidden;
    background: linear-gradient(180deg, var(--cover-top) 0%, var(--cover-top) 8%, var(--cover-mid) 45%, var(--cover-bottom) 100%);
  }
  .cover-photo {
    position: absolute;
    left: 260px;
    top: 347px;
    width: 432px;
    height: 670px;
  }
  .series-title {
    position: absolute;
    left: 54px;
    top: 84px;
    width: 600px;
    margin: 0;
    font-family: "Cinzel", serif;
    font-weight: 900;
    font-size: 62px;
    line-height: 1.08;
    letter-spacing: 1px;
    color: var(--ink-light);
  }
  .series-title .line {
    display: block;
    white-space: nowrap;
  }
  .book-title {
    position: absolute;
    left: 50px;
    top: 296px;
    margin: 0;
    font-family: "Roboto", sans-serif;
    font-weight: 300;
    color: var(--ink-light);
  }
  .book-title .lead {
    display: block;
    font-size: 27px;
    line-height: 1;
    margin-bottom: 18px;
    margin-left: 2px;
  }
  .book-title .line {
    display: block;
    font-size: 64px;
    line-height: 61px;
    letter-spacing: 1px;
  }
  .credits {
    position: absolute;
    left: 46px;
    top: 830px;
    font-family: "Cinzel", serif;
    font-weight: 700;
    color: var(--ink-light);
  }
  .credits .author {
    margin: 0;
    font-size: 30px;
    line-height: 1;
    letter-spacing: 1px;
  }
  .credits .quote {
    margin: 6px 0 0;
    font-size: 16px;
    line-height: 1;
    letter-spacing: 0.5px;
  }
  .credits .endorser {
    margin: 28px 0 0;
    font-size: 30px;
    line-height: 1;
    letter-spacing: 1px;
  }
  .credits .endorser-role {
    margin: 4px 0 0;
    font-size: 16px;
    line-height: 1;
    letter-spacing: 0.5px;
  }
</style>
</head>
<body>
<div class="canvas">
  <div class="cover">
    <svg class="cover-photo" viewBox="0 0 432 670" role="img" aria-label="Photo of a woman in a plaid shirt holding up red boxing gloves in a playful guard pose">
      <defs>
        <radialGradient id="photoTone" cx="60%" cy="45%" r="65%">
          <stop offset="0%" stop-color="#c8231f" stop-opacity="0.85"/>
          <stop offset="45%" stop-color="#7a1f24" stop-opacity="0.7"/>
          <stop offset="80%" stop-color="#2a2230" stop-opacity="0.55"/>
          <stop offset="100%" stop-color="#2a2230" stop-opacity="0"/>
        </radialGradient>
      </defs>
      <rect x="0" y="0" width="432" height="670" fill="url(#photoTone)"/>
    </svg>

    <h1 class="series-title">
      <span class="line">The Quiet</span>
      <span class="line">Harbor Method</span>
    </h1>

    <h2 class="book-title">
      <span class="lead">Grow a</span>
      <span class="line">FEARLESS</span>
      <span class="line">VENTURE</span>
    </h2>

    <div class="credits">
      <p class="author">Corla Vennick</p>
      <p class="quote">The most unusual business book you will read.</p>
      <p class="endorser">Jodi Marquenthal</p>
      <p class="endorser-role">Author of Founder Tidewalk</p>
    </div>
  </div>
</div>
</body>
</html>
```